Business Stationery - Business Cards - Letterheads, Compliment Slips

We need a new set of artwork designed for our client, they are a Construction Company, that also sell Kitchens, bathrooms and appliances.
They are an up and comping company that focus on quality and bespoke build. For them it is all about the quality of what they install, build or design. They have recently been awarded sole distributorship of a German kitchen brand Hannelore Moebel.
We need to present a quick job to them and provide some proofs for their new Artwork which encompasses all the elements of the company
The company name is the Tassel Group and we need to design a logo also.
Any Questions please let me know asap

Target Market(s)
Upmarket clients, or small Development companies.
Industry/Entity Type
Business
Look and feel
Each slider illustrates characteristics of the customer's brand and the style your logo design should communicate.

```html
<!DOCTYPE html>
<html lang="en">
<head>
<meta charset="utf-8">
<title>Tassel Group – Stationery Proofs</title>
<link rel="stylesheet" href="https://fonts.googleapis.com/css2?family=Roboto+Condensed:wght@300;400&family=Marcellus&display=swap">
<style>
  :root {
    --board: #d1d2d4;
    --paper: #ffffff;
    --brand-orange: #f15a2b;
    --brand-brown: #4a1e0e;
    --label-ink: #333333;
    --stripe-dark: #3a2a22;
    --stripe-rust: #8a3a1c;
  }
  * { margin: 0; padding: 0; box-sizing: border-box; }
  html, body { width: 1200px; height: 1000px; overflow: hidden; }
  body { background: var(--board); position: relative; }

  .proof-label {
    position: absolute;
    font-family: "Roboto Condensed", "Arial Narrow", sans-serif;
    font-weight: 300;
    font-size: 13px;
    line-height: 17px;
    color: var(--label-ink);
    text-transform: uppercase;
  }
  .proof-label--right-aligned { text-align: right; }

  .sheet { position: absolute; background: var(--paper); }

  .letterhead { width: 440px; height: 620px; top: 44px; }
  .letterhead--one { left: 156px; }
  .letterhead--two { left: 611px; }

  /* Identity lockup: one plain square plus the wordmark set in the brand text face */
  .brand-lockup {
    position: absolute;
    display: flex;
    flex-direction: column;
    align-items: center;
    font-family: "Marcellus", Georgia, serif;
    color: var(--brand-brown);
    letter-spacing: 0.08em;
    text-transform: uppercase;
    white-space: nowrap;
  }
  .brand-square { display: block; background: var(--brand-orange); }
  .brand-name { display: block; line-height: 1; }

  .letterhead .brand-lockup { top: 26px; right: 24px; font-size: 6px; gap: 3px; }
  .letterhead .brand-square { width: 46px; height: 42px; }

  .letterhead-footer-name {
    position: absolute;
    left: 22px;
    bottom: 32px;
    font-family: "Marcellus", Georgia, serif;
    font-size: 11px;
    letter-spacing: 0.14em;
    color: var(--brand-brown);
    text-transform: uppercase;
  }

  .letterhead-stripes {
    position: absolute;
    left: 0; right: 0;
    top: 591px;
    height: 9px;
  }
  .letterhead-stripes span { display: block; height: 2px; margin-bottom: 1px; }
  .stripe--dark { background: var(--stripe-dark); }
  .stripe--rust { background: var(--stripe-rust); }
  .stripe--orange { background: var(--brand-orange); }

  .logo-board { left: 154px; top: 691px; width: 282px; height: 280px; }
  .logo-board .brand-lockup { left: 27px; top: 22px; width: 228px; gap: 9px; }
  .logo-board .brand-square { width: 228px; height: 208px; }
  .logo-board .brand-name { font-size: 24px; letter-spacing: 0.09em; }

  .business-card { width: 211px; height: 146px; top: 722px; }
  .business-card--one { left: 602px; }
  .business-card--two { left: 835px; }
  .business-card .brand-lockup { font-size: 5px; gap: 2px; }
  .business-card--one .brand-lockup { top: 20px; right: 21px; }
  .business-card--one .brand-square { width: 34px; height: 30px; }
  .business-card--two .brand-lockup { top: 30px; left: 80px; font-size: 6px; gap: 3px; }
  .business-card--two .brand-square { width: 53px; height: 47px; }
  .card-rule {
    position: absolute;
    left: 0; right: 0;
    top: 121px;
    height: 3px;
    background: var(--brand-orange);
  }
</style>
</head>
<body>

  <div class="proof-label proof-label--right-aligned" style="right:1055px; top:45px;">Letterhead<br>Option 1</div>
  <div class="proof-label" style="left:1063px; top:45px;">Option 2</div>
  <div class="proof-label proof-label--right-aligned" style="right:1055px; top:694px;">Logo</div>
  <div class="proof-label proof-label--right-aligned" style="right:609px; top:722px;">Business Card<br>Option 1</div>
  <div class="proof-label" style="left:1056px; top:723px;">Option 2</div>

  <section class="sheet letterhead letterhead--one" aria-label="Letterhead option 1">
    <div class="brand-lockup"><span class="brand-square"></span></div>
    <p class="letterhead-footer-name">Tassel Group</p>
  </section>

  <section class="sheet letterhead letterhead--two" aria-label="Letterhead option 2">
    <div class="brand-lockup"><span class="brand-square"></span><span class="brand-name">Tassel Group</span></div>
    <div class="letterhead-stripes">
      <span class="stripe--dark"></span>
      <span class="stripe--rust"></span>
      <span class="stripe--orange"></span>
    </div>
  </section>

  <section class="sheet logo-board" aria-label="Logo">
    <div class="brand-lockup"><span class="brand-square"></span><span class="brand-name">Tassel Group</span></div>
  </section>

  <section class="sheet business-card business-card--one" aria-label="Business card option 1">
    <div class="brand-lockup"><span class="brand-square"></span><span class="brand-name">Tassel Group</span></div>
  </section>

  <section class="sheet business-card business-card--two" aria-label="Business card option 2">
    <div class="brand-lockup"><span class="brand-square"></span><span class="brand-name">Tassel Group</span></div>
    <div class="card-rule"></div>
  </section>

</body>
</html>
```